Wrenhollow Acres Organic Flower Farm, Farmer Florist

I am a flower grower and florist, so I do everything from the field to the vase. I want to include my website, phone, email and instagram

```html
<!DOCTYPE html>
<html lang="en">
<head>
<meta charset="utf-8">
<title>Wrenhollow Acres — Business Card</title>
<link rel="stylesheet" href="https://fonts.googleapis.com/css2?family=Noto+Serif:wght@400&display=swap">
<style>
  :root {
    --backdrop: #8a8b8a;
    --card-white: #ffffff;
    --maroon: #5e2e33;
    --blush: #f08a8e;
    --ink: #3d3d3d;
    --cream: #ffffff;
  }
  * { box-sizing: border-box; margin: 0; padding: 0; }
  html, body {
    width: 1188px;
    height: 1200px;
    overflow: hidden;
    background: var(--backdrop);
  }
  .canvas {
    position: relative;
    width: 1188px;
    height: 1200px;
  }
  .card {
    position: absolute;
    left: 245px;
    width: 696px;
    height: 386px;
    font-family: "Noto Serif", Georgia, serif;
  }
  .card--front { top: 159px; background: var(--card-white); }
  .card--back  { top: 627px; background: var(--maroon); }

  /* Brand: plain mark square + name */
  .brand {
    position: absolute;
    display: flex;
    flex-direction: column;
    align-items: center;
    transform: translateX(-50%);
    white-space: nowrap;
  }
  .brand__mark { display: block; }
  .brand__name {
    font-family: "Noto Serif", Georgia, serif;
    font-weight: 400;
    letter-spacing: 0.08em;
    line-height: 1;
  }

  .card--front .brand { left: 532px; top: 58px; }
  .card--front .brand__mark { width: 56px; height: 56px; background: var(--maroon); }
  .card--front .brand__name { font-size: 29px; color: var(--maroon); margin-top: 18px; }

  .card--back .brand { left: 349px; top: 96px; }
  .card--back .brand__mark { width: 84px; height: 84px; background: var(--blush); }
  .card--back .brand__name { font-size: 45px; color: var(--cream); margin-top: 24px; }

  /* Contact block */
  .person {
    position: absolute;
    left: 52px;
    top: 180px;
  }
  .person__name {
    font-size: 21px;
    color: var(--ink);
    line-height: 1.1;
    text-transform: uppercase;
  }
  .person__role {
    font-size: 20px;
    color: var(--blush);
    line-height: 1.1;
  }
  .contact-list {
    list-style: none;
    margin-top: 14px;
  }
  .contact-list__item {
    display: flex;
    align-items: center;
    height: 25px;
    font-size: 19px;
    color: var(--ink);
  }
  .contact-list__icon {
    width: 18px;
    height: 18px;
    margin-right: 7px;
    flex: none;
    fill: var(--maroon);
  }
</style>
</head>
<body>
<main class="canvas">

  <section class="card card--front" aria-label="Business card front">
    <div class="brand">
      <span class="brand__mark" aria-hidden="true"></span>
      <p class="brand__name">WRENHOLLOW</p>
    </div>

    <div class="person">
      <p class="person__name">Daniel Hartwell</p>
      <p class="person__role">Owner</p>
      <ul class="contact-list">
        <li class="contact-list__item">
          <svg class="contact-list__icon" viewBox="0 0 20 20" aria-hidden="true">
            <path d="M2 7c0-3 16-3 16 0v2h-4V7.5H6V9H2z"/>
            <path d="M5 10h10l2 7H3z"/>
          </svg>
          +56930472619
        </li>
        <li class="contact-list__item">
          <svg class="contact-list__icon" viewBox="0 0 20 20" aria-hidden="true">
            <path d="M1 4h18v12H1z M3 6l7 5 7-5v-.2H3z" fill-rule="evenodd"/>
          </svg>
          info@wrenhollow.com
        </li>
        <li class="contact-list__item">
          <svg class="contact-list__icon" viewBox="0 0 20 20" aria-hidden="true">
            <circle cx="10" cy="10" r="9"/>
            <ellipse cx="10" cy="10" rx="3.5" ry="8" stroke="#fff" stroke-width="1.2" fill="none"/>
            <path d="M2 10h16" stroke="#fff" stroke-width="1.2"/>
          </svg>
          www.wrenhollow.com
        </li>
        <li class="contact-list__item">
          <svg class="contact-list__icon" viewBox="0 0 20 20" aria-hidden="true">
            <rect x="2" y="2" width="16" height="16" rx="2"/>
          </svg>
          @wrenhollow
        </li>
      </ul>
    </div>
  </section>

  <section class="card card--back" aria-label="Business card back">
    <div class="brand">
      <span class="brand__mark" aria-hidden="true"></span>
      <p class="brand__name">WRENHOLLOW</p>
    </div>
  </section>

</main>
</body>
</html>
```